Flyer Frost Glow Cycle Tour
Zielgruppe
Wir sind DER Bikeshop in St. Moritz, welches auf 1800 m.ü.m. liegt. Wir verkaufen, vermieten uns servicen Bikes das ganze Jahr hindurch und haben auch 365 Tage im Jahr geöffnet. Wir sind die ersten, welche das Winterbiken für alle zugänglich gemacht haben und mit unseren Durafelt E-MTB ist das Fahren auf dem Schnee erstens sehr einfach und zweitens absolut sicher.
Aufgabenstellung
Flyerformat ist egal. Unsere Geschäftsfarben sind schwarz und gelb, der Hauptfont unseres Namens ist Marvelouz und wir arbeiten im High End Bereich. Gerne zwei Sprachen verwenden, evtl. Rückseite und Vorderseite gleich, nur die Sprachen ändern.
TEXT:
St. Moritz
Frost Glow Cycle Tour
Im Winter zu Biken ist ja schon verrückt, aber das ganze in der Nacht zu machen scheint ein Ding der Unmöglichkeit. Es ist das wahrscheinlich eines der coolsten Erlebnisse, welches es in St. Moritz im Winter gibt. Dank den Durafelt E-Bikes mit Spikes und unseren tollen Guides können Sie diese Ausfahrt auch sehr sicher erleben und sie ist für alle Personen, egal welchen Alters geeignet.
Auf speziellen Wunsch organisieren wir auch ein Outdoor-Abendessen, eine versteckte Alphütte zum Essen und Partymachen oder ganz einfach eine Champagnerpause im Pulverschnee dazu.
Dauer
1.5 – 2 Stunden
Inbegriffen
High End E-Bikes von Durafelt, Helm, Stirnlampe, heisses Getränk, Guide
Preis
ab Fr. 95.- pro Person (bei 8 Teilnehmern), Fr. 97.- bei 7 T., Fr. 100.- bei 6 T., Fr. 104.- bei 5 T., Fr. 110.- bei 4 T., Fr. 120.- bei 3 T., Fr. 140.- bei 2 T., Fr. 200.- bei einem Teilnemer.
Biking in winter is already crazy, but doing it at night seems impossible. It’s probably one of the coolest experiences you can have in St. Moritz in winter. Thanks to the Durafelt e-bikes with spikes and our great guides, you can also experience this ride very safely and it is suitable for all people, no matter what age.
On special request, we can also organise an outdoor dinner, a hidden alpine hut for eating and partying or simply a champagne break in the powder snow.
Duration
Included
High End E-Bikes von Durafelt, Helm, Stirnlampe, heisses Getränk, ..

```html
<!DOCTYPE html>
<html lang="de">
<head>
<meta charset="utf-8">
<title>Frost Glow Cycle Tour – Flyer DE / EN</title>
<link href="https://fonts.googleapis.com/css2?family=Alfa+Slab+One&family=Montserrat:wght@400;500;600;700;800&display=swap" rel="stylesheet">
<style>
  :root{
    --backdrop:#e9e9e9;
    --night:#1d1d20;
    --gold:#f5c518;
    --navy:#23427f;
    --white:#ffffff;
    --ink:#1d1d20;
  }
  *{box-sizing:border-box;margin:0;padding:0}
  html,body{width:1200px;height:800px;overflow:hidden;background:var(--backdrop)}
  body{font-family:"Montserrat",sans-serif;position:relative}

  .flyer{position:absolute;top:18px;width:540px;height:764px;background:var(--night);overflow:hidden;box-shadow:0 10px 26px rgba(0,0,0,.18)}
  .flyer-de{left:40px}
  .flyer-en{left:620px}

  .hero-photo{position:absolute;left:0;top:0;width:540px;height:300px;
    background:
      radial-gradient(ellipse 60% 35% at 45% 66%, rgba(255,255,255,.5), transparent 70%),
      radial-gradient(ellipse 50% 30% at 40% 40%, rgba(230,140,50,.55), transparent 70%),
      radial-gradient(ellipse 40% 30% at 35% 80%, rgba(200,40,40,.4), transparent 70%),
      linear-gradient(180deg,#3a2619 0%,#5a3a22 35%,#3d3540 62%,#1d1d20 100%);}
  .brand{position:absolute;top:28px;left:0;width:100%;text-align:center;color:var(--white);font-weight:800;font-size:19px;letter-spacing:9px}
  .title{position:absolute;top:212px;left:0;width:100%;text-align:center;font-family:"Alfa Slab One",serif;font-weight:400;color:var(--white);font-size:36px;letter-spacing:1px;line-height:44px}
  .ribbon{position:absolute;top:260px;left:50px;width:440px;height:42px}
  .ribbon-text{position:absolute;top:260px;left:0;width:100%;height:42px;line-height:42px;text-align:center;font-family:"Alfa Slab One",serif;font-weight:400;color:var(--ink);font-size:21px;letter-spacing:1.5px}

  .intro{position:absolute;top:318px;left:35px;width:470px;text-align:center;color:var(--white);font-size:8.8px;line-height:1.5}
  .intro p+p{margin-top:7px}
  .intro .place{color:var(--gold)}

  .shapes{position:absolute;left:0;top:0}
  .included{position:absolute;top:471px;left:0;width:540px;height:28px;line-height:28px;text-align:center;color:var(--white);font-weight:700;font-size:8px;transform:rotate(3.18deg);text-transform:uppercase;white-space:nowrap}

  .deal-badge{position:absolute;top:540px;left:30px;background:var(--navy);color:var(--white);font-family:"Alfa Slab One",serif;font-size:11px;padding:3px 10px;border-radius:10px;letter-spacing:1px}
  .deal-main{position:absolute;top:562px;left:22px;width:132px;text-align:center;color:var(--navy)}
  .deal-main .amount{font-family:"Alfa Slab One",serif;font-size:28px;line-height:34px}
  .deal-main .amount small{font-size:13px}
  .deal-main .note{font-size:10.5px;line-height:1.3;color:var(--ink)}

  .price-grid{position:absolute;top:540px;left:160px;display:grid;grid-template-columns:repeat(4,92px);row-gap:8px}
  .price{text-align:center;color:var(--ink);font-size:7.5px;line-height:1.3}
  .price .amount{font-family:"Alfa Slab One",serif;color:var(--navy);font-size:17px;line-height:20px}
  .price .amount small{font-size:8px}

  .gallery{position:absolute;top:642px;left:24px;display:flex;gap:16px}
  .gallery-photo{width:136px;height:84px;border:4px solid var(--white);border-radius:10px;box-shadow:0 3px 8px rgba(0,0,0,.25)}
  .photo-village{background:linear-gradient(180deg,#2b3a66 0%,#4a5a8a 45%,#c58a3a 80%,#2a2a3a 100%)}
  .photo-fire{background:linear-gradient(180deg,#3a3a4a 0%,#8a5a2a 50%,#f0a040 75%,#e8eef5 100%)}
  .photo-riders{background:linear-gradient(180deg,#1e2636 0%,#4a5466 50%,#d8dde6 100%)}

  .duration{position:absolute;top:618px;left:448px;width:84px;height:84px;border-radius:50%;background:var(--navy);border:2px solid var(--white);color:var(--white);display:flex;flex-direction:column;align-items:center;justify-content:center;font-weight:700;font-size:11.5px;line-height:1.2;text-align:center}

  .contacts{position:absolute;top:740px;left:0;width:540px;display:flex;justify-content:center;gap:14px;font-size:7.5px;font-weight:600;color:var(--ink);white-space:nowrap}
  .contact{display:flex;align-items:center;gap:4px}
  .contact svg{width:10px;height:10px}
</style>
</head>
<body>

<svg width="0" height="0" style="position:absolute" aria-hidden="true">
  <defs>
    <symbol id="icon-pin" viewBox="0 0 12 12"><path d="M6 0.5a4 4 0 0 1 4 4c0 3-4 7-4 7s-4-4-4-7a4 4 0 0 1 4-4z" fill="#23427f"/><circle cx="6" cy="4.5" r="1.4" fill="#fff"/></symbol>
    <symbol id="icon-phone" viewBox="0 0 12 12"><path d="M2.5 1l2 0.4 1 2.4-1.3 1a6 6 0 0 0 3 3l1-1.3 2.4 1 .4 2-1.3 1.2C5 10.5 1.5 7 1.3 2.3z" fill="#23427f"/></symbol>
    <symbol id="icon-mail" viewBox="0 0 12 12"><rect x="0.5" y="2" width="11" height="8" fill="#23427f"/><path d="M0.5 2.5L6 6.5l5.5-4" stroke="#fff" fill="none"/></symbol>
    <symbol id="icon-web" viewBox="0 0 12 12"><circle cx="6" cy="6" r="5" fill="none" stroke="#23427f" stroke-width="1.3"/><ellipse cx="6" cy="6" rx="2" ry="5" fill="none" stroke="#23427f"/><line x1="1" y1="6" x2="11" y2="6" stroke="#23427f"/></symbol>
  </defs>
</svg>

<!-- German side -->
<article class="flyer flyer-de" lang="de">
  <div class="hero-photo" role="img" aria-label="Nachtfoto: Fahrer mit Stirnlampen auf E-Bikes im Schnee über dem beleuchteten St. Moritz"></div>
  <div class="brand">RIDEHAUS</div>
  <h1 class="title">ST. MORITZ</h1>
  <svg class="ribbon" viewBox="0 0 440 42" aria-hidden="true"><polygon points="0,0 440,0 424,21 440,42 0,42 16,21" fill="#f5c518"/></svg>
  <h2 class="ribbon-text">FROST GLOW CYCLE TOUR</h2>

  <div class="intro">
    <p>Im Winter zu Biken ist ja schon verrückt, aber das ganze in der Nacht zu machen scheint ein Ding der Unmöglichkeit. Es ist das wahrscheinlich eines der coolsten Erlebnisse, welches es in <span class="place">St. Moritz</span> im Winter gibt. Dank den Durafelt E-Bikes mit Spikes und unseren tollen Guides können Sie diese Ausfahrt auch sehr sicher erleben und sie ist für alle Personen, egal welchen Alters geeignet.</p>
    <p>Auf speziellen Wunsch organisieren wir auch ein Outdoor-Abendessen, eine versteckte Alphütte zum Essen und Partymachen oder ganz einfach eine Champagnerpause im Pulverschnee dazu.</p>
  </div>

  <svg class="shapes" width="540" height="764" viewBox="0 0 540 764" aria-hidden="true">
    <polygon points="0,470 540,500 540,528 0,498" fill="#23427f"/>
    <polygon points="0,498 540,528 540,764 0,764" fill="#f5c518"/>
    <path d="M0,690 Q270,736 540,664 L540,764 L0,764 Z" fill="#fff"/>
  </svg>

  <div class="included">Inbegriffen: High End E-Bikes von Durafelt, Helm, Stirnlampe, heisses Getränk, Guide</div>

  <div class="deal-badge">BEST DEALS!</div>
  <div class="deal-main">
    <div class="amount"><small>FR.</small> 95.-</div>
    <div class="note">pro Person<br>(bei 8 Teilnehmern)</div>
  </div>

  <div class="price-grid">
    <div class="price"><div class="amount"><small>FR.</small>97.-</div>pro Person<br>(bei 7 Teilnehmern)</div>
    <div class="price"><div class="amount"><small>FR.</small>100.-</div>pro Person<br>(bei 6 Teilnehmern)</div>
    <div class="price"><div class="amount"><small>FR.</small>104.-</div>pro Person<br>(bei 5 Teilnehmern)</div>
    <div class="price"><div class="amount"><small>FR.</small>110.-</div>pro Person<br>(bei 4 Teilnehmern)</div>
    <div class="price"><div class="amount"><small>FR.</small>120.-</div>pro Person<br>(bei 3 Teilnehmern)</div>
    <div class="price"><div class="amount"><small>FR.</small>140.-</div>pro Person<br>(bei 2 Teilnehmern)</div>
    <div class="price"><div class="amount"><small>FR.</small>200.-</div>pro Person<br>(bei 1 Teilnehmer)</div>
  </div>

  <div class="gallery">
    <div class="gallery-photo photo-village" role="img" aria-label="Lichter von St. Moritz in der Dämmerung unter verschneiten Bergen"></div>
    <div class="gallery-photo photo-fire" role="img" aria-label="Lagerfeuer mit Kochgestell im Schnee bei Nacht"></div>
    <div class="gallery-photo photo-riders" role="img" aria-label="Fahrer auf E-Bikes zwischen beleuchteten, verschneiten Bäumen"></div>
  </div>

  <div class="duration">Dauer:<span>2 Stunden</span></div>

  <div class="contacts">
    <span class="contact"><svg><use href="#icon-pin"/></svg>Via Lunga 8, 7500 St. Moritz</span>
    <span class="contact"><svg><use href="#icon-phone"/></svg>+41 81 555 01 20</span>
    <span class="contact"><svg><use href="#icon-mail"/></svg>info@ridehaus-alpin.ch</span>
    <span class="contact"><svg><use href="#icon-web"/></svg>www.ridehaus-alpin.ch</span>
  </div>
</article>

<!-- English side -->
<article class="flyer flyer-en" lang="en">
  <div class="hero-photo" role="img" aria-label="Night photo of riders with headlamps on snowy e-bikes above the lit village of St. Moritz"></div>
  <div class="brand">RIDEHAUS</div>
  <h1 class="title">ST. MORITZ</h1>
  <svg class="ribbon" viewBox="0 0 440 42" aria-hidden="true"><polygon points="0,0 440,0 424,21 440,42 0,42 16,21" fill="#f5c518"/></svg>
  <h2 class="ribbon-text">FROST GLOW CYCLE TOUR</h2>

  <div class="intro">
    <p>Biking in winter is already crazy, but doing it at night seems impossible. It’s probably one of the coolest experiences you can have in <span class="place">St. Moritz</span> in winter. Thanks to the Durafelt e-bikes with spikes and our great guides, you can also experience this ride very safely and it is suitable for all people, no matter what age.</p>
    <p>On special request, we can also organise an outdoor dinner, a hidden alpine hut for eating and partying or simply a champagne break in the powder snow.</p>
  </div>

  <svg class="shapes" width="540" height="764" viewBox="0 0 540 764" aria-hidden="true">
    <polygon points="0,470 540,500 540,528 0,498" fill="#23427f"/>
    <polygon points="0,498 540,528 540,764 0,764" fill="#f5c518"/>
    <path d="M0,690 Q270,736 540,664 L540,764 L0,764 Z" fill="#fff"/>
  </svg>

  <div class="included">Included: High End E-Bikes von Durafelt, Helm, Stirnlampe, heisses Getränk, Guide</div>

  <div class="deal-badge">BEST DEALS!</div>
  <div class="deal-main">
    <div class="amount"><small>FR.</small> 95.-</div>
    <div class="note">per person<br>(with 8 participants)</div>
  </div>

  <div class="price-grid">
    <div class="price"><div class="amount"><small>FR.</small>97.-</div>per person<br>(with 7 participants)</div>
    <div class="price"><div class="amount"><small>FR.</small>100.-</div>per person<br>(with 6 participants)</div>
    <div class="price"><div class="amount"><small>FR.</small>104.-</div>per person<br>(with 5 participants)</div>
    <div class="price"><div class="amount"><small>FR.</small>110.-</div>per person<br>(with 4 participants)</div>
    <div class="price"><div class="amount"><small>FR.</small>120.-</div>per person<br>(with 3 participants)</div>
    <div class="price"><div class="amount"><small>FR.</small>140.-</div>per person<br>(with 2 participants)</div>
    <div class="price"><div class="amount"><small>FR.</small>200.-</div>per person<br>(with 1 participant)</div>
  </div>

  <div class="gallery">
    <div class="gallery-photo photo-village" role="img" aria-label="St. Moritz village lights at dusk below snowy mountains"></div>
    <div class="gallery-photo photo-fire" role="img" aria-label="Campfire with a cooking tripod in the snow at night"></div>
    <div class="gallery-photo photo-riders" role="img" aria-label="Riders on e-bikes among lit snowy trees at night"></div>
  </div>

  <div class="duration">Duration:<span>2 Stunden</span></div>

  <div class="contacts">
    <span class="contact"><svg><use href="#icon-pin"/></svg>Via Lunga 8, 7500 St. Moritz</span>
    <span class="contact"><svg><use href="#icon-phone"/></svg>+41 81 555 01 20</span>
    <span class="contact"><svg><use href="#icon-mail"/></svg>info@ridehaus-alpin.ch</span>
    <span class="contact"><svg><use href="#icon-web"/></svg>www.ridehaus-alpin.ch</span>
  </div>
</article>

</body>
</html>
```